Finiding oppertunites in Real Estate 6.15.20

size of ad 7” x 9.6”
1-I like the ad to stand out and attract people's attention.
2-you should be able to see the text of the ad clearly .. see the attachment anything in yellow is instructions.
3-the list of topics should not be the main part of the ad
4-if you decide you want a picture or vector of a person .. (you decide)
then it should be a white male about 25-30 years old wearing a solid white or blue shirt and not long hair.
5-leave 1 inch for footer
see attachment
Good luck

Target Market(s)

potential male students 25-35 years of age

Industry/Entity Type

Education

Requirements
Must have
• will stand out and people would want to see it.
should be able to read the words of ad
Nice to have
• how to make money in real estate on one line

```html
<!DOCTYPE html>
<html lang="en">
<head>
<meta charset="utf-8">
<title>Real Estate Career Course Flyers</title>
<link rel="stylesheet" href="https://fonts.googleapis.com/css2?family=Bebas+Neue&family=Roboto+Condensed:wght@300;400;700&display=swap">
<style>
  :root {
    --stage: #5c5c5c;
    --paper: #ffffff;
    --gold: #f9b506;
    --royal: #0a47b0;
    --navy: #062f86;
    --ink: #1c1c1c;
    --red: #dd0000;
    --band-gray: #eeeeee;
    --silver: #ececec;
    --silver-edge: #f5f5f5;
    --gold-edge: #f2f2f2;
  }
  * { box-sizing: border-box; margin: 0; padding: 0; }
  html, body { width: 1200px; height: 780px; overflow: hidden; }
  body { background: var(--stage); position: relative; font-family: "Roboto Condensed", Arial, sans-serif; }

  .flyer {
    position: absolute; top: 30px; width: 533px; height: 730px;
    background: var(--paper); overflow: hidden;
  }
  .flyer--gold { left: 44px; --accent-fill: var(--gold); --accent-edge: var(--gold-edge); }
  .flyer--silver { left: 625px; --accent-fill: var(--silver); --accent-edge: var(--silver-edge); }

  .swoosh { position: absolute; left: 0; top: 0; width: 260px; height: 656px; }
  .swoosh .edge { fill: var(--accent-edge); }
  .swoosh .fill { fill: var(--accent-fill); }

  .figure-area {
    position: absolute; left: 10px; top: 113px; width: 215px; height: 542px;
    border-radius: 90px 90px 20px 20px;
    background: linear-gradient(180deg, #f3f3f3 0%, #ffffff 40%, #3f4a5c 58%, #3b4658 95%, #2a2d36 100%);
    opacity: .92;
  }

  .headline { position: absolute; right: 16px; text-align: right; font-family: "Bebas Neue", Impact, sans-serif; line-height: 1; }
  .headline--gold { top: 22px; font-size: 70px; color: var(--gold); }
  .headline--blue { top: 77px; font-size: 70px; color: var(--royal); letter-spacing: -0.5px; }

  .question { position: absolute; right: 16px; top: 140px; font-size: 26px; font-weight: 400; color: var(--ink); letter-spacing: -0.4px; }

  .audience { position: absolute; right: 24px; top: 198px; text-align: right; font-size: 20px; font-weight: 300; line-height: 23px; color: var(--royal); }

  .promise { position: absolute; right: 23px; top: 263px; text-align: right; font-weight: 700; font-size: 33px; line-height: 30px; letter-spacing: -0.6px; }
  .promise .dark { color: var(--ink); }
  .promise .gold { color: var(--gold); }

  .session-band { position: absolute; left: 284px; top: 386px; width: 249px; height: 26px; background: var(--red); }
  .session-band span { position: absolute; left: 39px; top: 3px; font-family: "Bebas Neue", Impact, sans-serif; font-size: 22px; line-height: 1; color: #fff; letter-spacing: .3px; }
  .date-band { position: absolute; left: 284px; top: 412px; width: 249px; height: 61px; background: var(--band-gray); }
  .date-band .label { position: absolute; left: 41px; top: 4px; font-weight: 700; font-size: 18px; color: var(--ink); line-height: 1; }
  .date-band .date { position: absolute; left: 30px; top: 20px; font-weight: 700; font-size: 42px; color: var(--ink); line-height: 1; letter-spacing: -1px; }

  .seal { position: absolute; left: 198px; top: 376px; width: 110px; height: 110px; }
  .seal .points { fill: var(--royal); }
  .seal-text { position: absolute; left: 198px; top: 400px; width: 110px; text-align: center; font-family: "Bebas Neue", Impact, sans-serif; font-size: 29px; line-height: 25px; color: #fff; }

  .topics-title { position: absolute; left: 248px; top: 499px; font-weight: 700; font-size: 16px; color: var(--royal); }
  .topics { position: absolute; top: 534px; list-style: none; font-size: 13px; line-height: 15.9px; color: var(--ink); }
  .topics--left { left: 244px; }
  .topics--right { left: 412px; }
  .topics li { position: relative; padding-left: 10px; }
  .topics li::before { content: ""; position: absolute; left: 0; top: 6px; width: 4px; height: 4px; border-radius: 50%; background: var(--gold); }
</style>
</head>
<body>

<section class="flyer flyer--gold">
  <svg class="swoosh" viewBox="0 0 260 656" aria-hidden="true">
    <path class="edge" d="M0 0 H164 C205 40 212 140 180 240 C160 300 140 330 150 420 C230 470 270 560 245 656 H0 Z"/>
    <path class="fill" d="M0 0 H154 C192 40 200 140 170 240 C150 300 130 330 142 420 C218 470 258 560 237 656 H0 Z"/>
  </svg>
  <div class="figure-area" role="img" aria-label="Young man in a white shirt and grey trousers holding an open laptop"></div>

  <h1 class="headline headline--gold">REAL ESTATE</h1>
  <h2 class="headline headline--blue">CAREER COURSE</h2>
  <p class="question">How to Make Money In In Real Estate?</p>
  <p class="audience">For those who have started or<br>would like to go into Real Estate</p>
  <p class="promise"><span class="dark">AN INVESTMENT IN</span><br><span class="gold">KNOWLEDGE OPENS UP<br>UNTOLD OPPORTUNITIE</span></p>

  <div class="session-band"><span>12 SESSION COURSE</span></div>
  <div class="date-band"><span class="label">CLASSES STARTING</span><span class="date">JUNE 16</span></div>
  <svg class="seal" viewBox="0 0 110 110" aria-hidden="true">
    <g class="points" transform="translate(55 55)">
      <rect x="-37" y="-37" width="74" height="74"/>
      <rect x="-37" y="-37" width="74" height="74" transform="rotate(15)"/>
      <rect x="-37" y="-37" width="74" height="74" transform="rotate(30)"/>
      <rect x="-37" y="-37" width="74" height="74" transform="rotate(45)"/>
      <rect x="-37" y="-37" width="74" height="74" transform="rotate(60)"/>
      <rect x="-37" y="-37" width="74" height="74" transform="rotate(75)"/>
    </g>
    <circle cx="55" cy="55" r="42" fill="#083a9a"/>
  </svg>
  <p class="seal-text">REMOTE<br>SESSIONS</p>

  <h3 class="topics-title">A PARTIAL LISTING OF TOPICS :</h3>
  <ul class="topics topics--left">
    <li>Single-family</li><li>Multifamily</li><li>Management</li><li>Real Estate Concepts</li><li>Real Estate law</li><li>Investment properties</li><li>Foreclosures</li>
  </ul>
  <ul class="topics topics--right">
    <li>Rehab</li><li>Foreclosures</li><li>Short sales</li><li>Development</li><li>Finical modeling</li><li>HUD properties</li><li>Due Diligencee</li>
  </ul>
</section>

<section class="flyer flyer--silver">
  <svg class="swoosh" viewBox="0 0 260 656" aria-hidden="true">
    <path class="edge" d="M0 0 H164 C205 40 212 140 180 240 C160 300 140 330 150 420 C230 470 270 560 245 656 H0 Z"/>
    <path class="fill" d="M0 0 H154 C192 40 200 140 170 240 C150 300 130 330 142 420 C218 470 258 560 237 656 H0 Z"/>
  </svg>
  <div class="figure-area" role="img" aria-label="Young man in a white shirt and grey trousers holding an open laptop"></div>

  <h1 class="headline headline--gold">REAL ESTATE</h1>
  <h2 class="headline headline--blue">CAREER COURSE</h2>
  <p class="question">How to Make Money In In Real Estate?</p>
  <p class="audience">For those who have started or<br>would like to go into Real Estate</p>
  <p class="promise"><span class="dark">AN INVESTMENT IN</span><br><span class="gold">KNOWLEDGE OPENS UP<br>UNTOLD OPPORTUNITIE</span></p>

  <div class="session-band"><span>12 SESSION COURSE</span></div>
  <div class="date-band"><span class="label">CLASSES STARTING</span><span class="date">JUNE 16</span></div>
  <svg class="seal" viewBox="0 0 110 110" aria-hidden="true">
    <g class="points" transform="translate(55 55)">
      <rect x="-37" y="-37" width="74" height="74"/>
      <rect x="-37" y="-37" width="74" height="74" transform="rotate(15)"/>
      <rect x="-37" y="-37" width="74" height="74" transform="rotate(30)"/>
      <rect x="-37" y="-37" width="74" height="74" transform="rotate(45)"/>
      <rect x="-37" y="-37" width="74" height="74" transform="rotate(60)"/>
      <rect x="-37" y="-37" width="74" height="74" transform="rotate(75)"/>
    </g>
    <circle cx="55" cy="55" r="42" fill="#083a9a"/>
  </svg>
  <p class="seal-text">REMOTE<br>SESSIONS</p>

  <h3 class="topics-title">A PARTIAL LISTING OF TOPICS :</h3>
  <ul class="topics topics--left">
    <li>Single-family</li><li>Multifamily</li><li>Management</li><li>Real Estate Concepts</li><li>Real Estate law</li><li>Investment properties</li><li>Foreclosures</li>
  </ul>
  <ul class="topics topics--right">
    <li>Rehab</li><li>Foreclosures</li><li>Short sales</li><li>Development</li><li>Finical modeling</li><li>HUD properties</li><li>Due Diligencee</li>
  </ul>
</section>

</body>
</html>
```